Wordpress Design Project - QuorvanLabs

I would like our existing old website at www.quorvanlabs.example to be redesigned to a more modern attractive site using Wordpress, a total of 5 web pages. And also installed onto our new web hosting site. Please visit the existing website using Microsoft Internet explorer to see the content.
The new site must be compatible with all popular web browsers and mobile devices (if possible).
There should be a contact button available on each page with an associated form in case an interested person wants to contact us. This form must be spam proof not allowing automated crawlers from activating it.
Updates

There are only 5 pages web pages to this QuorvanLabs project.

Industry/Entity Type

Internet

```html
<!DOCTYPE html>
<html lang="en">
<head>
<meta charset="utf-8">
<title>QuorvanLabs</title>
<link rel="stylesheet" href="https://fonts.googleapis.com/css2?family=Bebas+Neue&family=PT+Sans:wght@400;700&family=Oswald:wght@400;500&family=Archivo+Black&display=swap">
<style>
:root{
  --paper:#efe9dc;
  --paper-dark:#e6dfd0;
  --nav-active:#3d6db5;
  --nav-text:#1d4f8c;
  --ink:#2a2a2a;
  --deep:#0e3a4a;
  --teal:#0b9ac6;
  --footer-dark:#1f2d38;
  --button:#2a9ff0;
}
*{box-sizing:border-box;margin:0;padding:0}
html,body{width:1200px;height:619px;overflow:hidden}
body{position:relative;background:var(--paper);font-family:"PT Sans",sans-serif;color:var(--ink)}
.hero{position:absolute;left:0;top:0;width:795px;height:534px;
  background:radial-gradient(circle at 40% 55%,#e9f7fd 0%,#8fd3f0 30%,#3aa7d8 60%,#0c5e8a 100%)}
.brand{position:absolute;left:26px;top:36px;width:226px;height:76px;background:#fff;display:flex;align-items:center;padding-left:10px;gap:10px}
.brand-mark{width:40px;height:40px;border-radius:50%;background:var(--nav-text)}
.brand-text{display:flex;flex-direction:column}
.brand-name{font-size:22px;font-weight:700;color:var(--nav-text)}
.brand-tag{font-size:7px;font-weight:700;color:var(--nav-text);margin-top:1px}
.main-nav{position:absolute;left:26px;top:112px;width:226px;list-style:none}
.main-nav li{height:37.5px;background:#fbfbfb;border-bottom:1px solid #e2e2e2;display:flex;align-items:center;padding-left:18px;font-size:11.5px;letter-spacing:2px;color:var(--nav-text)}
.main-nav li.active{background:var(--nav-active);color:#fff}
.main-nav svg{width:12px;height:12px;margin-right:14px;fill:#222}
.main-nav li.active svg{fill:#fff}
.helpdesk{position:absolute;left:0;top:357px;width:167px;height:34px;background:var(--deep);color:#fff;font-family:"Archivo Black",sans-serif;font-size:14px;letter-spacing:1.5px;line-height:34px;padding-left:6px}
.helpdesk-badge{position:absolute;left:167px;top:357px;width:39px;height:34px;background:#fff}
.helpdesk-badge i{position:absolute;left:11px;top:8px;width:18px;height:18px;border-radius:50%;background:#d24343}
.sales{position:absolute;left:0;top:392px;width:290px;height:66px;background:#fff;padding:8px 0 0 6px;box-shadow:0 1px 3px rgba(0,0,0,.3)}
.sales-number{font-family:"Oswald",sans-serif;font-size:28px;letter-spacing:2px;color:#8a8a8a;line-height:28px}
.sales-label{font-size:15px;color:#8a8a8a;letter-spacing:1px}
.sales svg{position:absolute;right:22px;top:10px}
.dots{position:absolute;left:45px;top:494px;display:flex;gap:5px}
.dots span{width:13px;height:13px;border-radius:50%;border:2px solid #0a2c3c;background:#0a0a0a}
.dots span+span{background:#27b3e8}
.contact{position:absolute;left:795px;top:0;width:405px;height:534px;overflow:hidden}
.contact h2{position:absolute;left:25px;top:33px;font-family:"Bebas Neue",sans-serif;font-size:22px;letter-spacing:1.5px;font-weight:400;padding-right:10px;border-bottom:1px solid #c9c2b4;width:202px;padding-bottom:2px}
.field{position:absolute;background:linear-gradient(#f6f6f6,#e9e9e9);box-shadow:1px 1px 2px rgba(0,0,0,.25);font-family:"Bebas Neue",sans-serif;font-size:14px;letter-spacing:1.5px;color:#9a9a9a;padding:4px 8px}
.field.name{left:26px;top:73px;width:151px;height:25px}
.field.email{left:188px;top:73px;width:152px;height:25px}
.field.message{left:26px;top:109px;width:314px;height:63px}
.send{position:absolute;left:123px;top:183px;width:122px;height:26px;background:linear-gradient(#4fb8ff,var(--button));font-family:"Bebas Neue",sans-serif;font-size:15px;letter-spacing:1.5px;color:#08203a;text-align:center;line-height:27px}
.about{position:absolute;left:27px;top:226px;width:315px;font-size:11px;line-height:11.6px;letter-spacing:1px;text-align:justify}
.about p{margin-bottom:11.6px}
.about a{color:#1a5fb0}
.scrollbar{position:absolute;left:1166px;top:27px;width:13px;height:498px;background:#f7f3ea}
.scrollbar i{position:absolute;left:0;top:0;width:13px;height:106px;background:var(--teal)}
.footer-nav{position:absolute;left:30px;top:555px;display:flex;gap:15px;font-size:12px;letter-spacing:1.5px}
.footer-mail{position:absolute;left:30px;top:578px;font-size:11px;letter-spacing:1px}
.social{position:absolute;left:789px;top:534px;width:328px;height:85px;background:var(--footer-dark);color:#d4dbe0}
.follow{position:absolute;left:49px;top:36px;font-size:10.5px;letter-spacing:1.5px}
.social .circle{position:absolute;top:23px;width:38px;height:38px;border-radius:50%;background:#fff}
.social .divider{position:absolute;left:242px;top:25px;width:1px;height:40px;background:#55636e}
.social .call{position:absolute;left:260px;top:23px;width:38px;height:38px;border-radius:50%;background:var(--teal);display:flex;align-items:center;justify-content:center}
.social .call-label{position:absolute;left:256px;top:67px;font-size:11px;letter-spacing:1.5px}
.search{position:absolute;left:1117px;top:534px;width:83px;height:85px;background:var(--teal);display:flex;align-items:center;justify-content:center}
</style>
</head>
<body>
<div class="hero" role="img" aria-label="Glowing globe with network arcs over blueprint drawings"></div>

<div class="brand"><span class="brand-mark"></span><div class="brand-text"><span class="brand-name">QuorvanLabs</span><span class="brand-tag">A Leading Edge Technology Company</span></div></div>

<ul class="main-nav">
  <li class="active"><svg viewBox="0 0 12 12"><path d="M6 1 1 6h2v5h6V6h2z"/></svg>HOME</li>
  <li><svg viewBox="0 0 12 12"><circle cx="6" cy="3.5" r="2.5"/><path d="M1.5 12a4.5 4.5 0 0 1 9 0z"/></svg>ABOUT US</li>
  <li><svg viewBox="0 0 12 12"><rect x="2" y="3" width="7" height="9"/><rect x="4" y="1" width="7" height="9"/></svg>PRODUCTS</li>
  <li><svg viewBox="0 0 12 12"><circle cx="4" cy="8" r="3"/><circle cx="9" cy="3" r="2.3"/></svg>SERVICES</li>
  <li><svg viewBox="0 0 12 12"><path d="M1 4c0-2 10-2 10 0v1H8V4H4v1H1zM3 6h6l1 5H2z"/></svg>CONTACT US</li>
</ul>

<div class="helpdesk">24 X 7 HELP DESK</div>
<div class="helpdesk-badge"><i></i></div>
<div class="sales">
  <div class="sales-number">1.888.555.0142</div>
  <div class="sales-label">Sales Contact -Toll Free</div>
  <svg width="50" height="50" viewBox="0 0 50 50"><circle cx="25" cy="25" r="23" fill="none" stroke="#1e8fc8" stroke-width="3"/><path d="M20 13c-4 2-4 8-2 13s6 10 10 11l3-5-4-3-2 2c-2-1-4-5-4-8l3-1-1-5z" fill="#1e8fc8"/></svg>
</div>
<div class="dots"><span></span><span></span></div>

<section class="contact">
  <h2>CONTACT US</h2>
  <div class="field name">NAME</div>
  <div class="field email">EMAIL</div>
  <div class="field message">MESSAGE</div>
  <div class="send">SEND MESSAGE</div>
  <div class="about">
    <p>QuorvanLabs provides complete telephone VoIP PBX solutions for businesses large and small.</p>
    <p>Our team of telecom engineers will design and install the best business telephone VoIP PBX solution for your requirements. System features include: standard and advanced PBX call control actions, video telephone calling, toll free calling any where in the world, and 24x7 support.</p>
    <p>For more details, <a href="#">click here</a></p>
    <p>We also provide complete wired and wireless LAN/WAN/IP solutions and services for data, voice, Internet and private intranet networks to a variety of industries, including hospitality, industrial, commercial and institutional groups.</p>
    <p>Our Support Services Division call center provides 24 x 7 help desk technical support services for industries including telecommunications, commercial and lodging / hotel.</p>
  </div>
</section>
<div class="scrollbar"><i></i></div>

<nav class="footer-nav"><span>HOME</span><span>ABOUT US</span><span>PRODUCTS</span><span>SERVICES</span><span>CONTACT US</span></nav>
<div class="footer-mail">info@quorvanengineering.example</div>

<div class="social">
  <span class="follow">FOLLOW US</span>
  <span class="circle" style="left:131px" aria-label="Social profile"></span>
  <span class="circle" style="left:189px" aria-label="Social profile"></span>
  <span class="divider"></span>
  <span class="call"><svg width="20" height="20" viewBox="0 0 20 20"><path d="M5 2C2 3 2 8 5 12s7 6 9 6l2-3-3-3-2 1c-2-1-4-4-4-6l2-1-1-4z" fill="#fff"/></svg></span>
  <span class="call-label">CONTACT</span>
</div>
<div class="search"><svg width="44" height="44" viewBox="0 0 44 44"><circle cx="18" cy="18" r="13" fill="none" stroke="#fff" stroke-width="5"/><path d="M27 27l12 12" stroke="#fff" stroke-width="7" stroke-linecap="round"/></svg></div>
</body>
</html>
```